Bravel Acres Business Cards

design business cards for our new business should match my Corvane Quotations business cards

Contact Information for Business Card

2817 W 68th N St
Tulsa, OK 74592

Requirements
Must have
• should match logo colors

```html
<!DOCTYPE html>
<html lang="en">
<head>
<meta charset="utf-8">
<title>Bravel Acres Business Cards</title>
<link href="https://fonts.googleapis.com/css2?family=Arimo:wght@400;700&display=swap" rel="stylesheet">
<style>
  :root {
    --page: #2a2624;
    --card: #0f2c35;
    --green: #7ac143;
    --teal: #1aafb6;
    --ink-soft: #c9d1d3;
    --rule: #8a979b;
    --white: #ffffff;
  }
  * { margin: 0; padding: 0; box-sizing: border-box; }
  html, body { width: 1200px; height: 842px; overflow: hidden; }
  body {
    background: var(--page);
    font-family: "Arimo", Arial, sans-serif;
    display: flex;
    align-items: center;
    justify-content: center;
    gap: 40px;
  }
  .card {
    position: relative;
    width: 540px;
    height: 309px;
    background: var(--card);
    overflow: hidden;
    box-shadow: 0 10px 30px rgba(0,0,0,0.45);
  }
  .band {
    position: absolute;
    left: 0; right: 0;
    height: 9px;
    background: linear-gradient(90deg, var(--green) 0%, var(--green) 45%, var(--teal) 62%, var(--teal) 100%);
  }
  .band--top { top: 0; }
  .band--bottom { bottom: 0; }
  .details {
    position: absolute;
    left: 0; right: 0; top: 58px;
    text-align: center;
    color: var(--ink-soft);
  }
  .details__name {
    font-weight: 700;
    font-size: 19px;
    letter-spacing: 0.3px;
    color: var(--green);
    background: linear-gradient(90deg, var(--green), var(--teal));
    -webkit-background-clip: text;
    background-clip: text;
    color: transparent;
  }
  .details__role { font-size: 13.5px; margin-top: 1px; }
  .details__rule {
    width: 160px; height: 1px; background: var(--rule);
    margin: 10px auto;
  }
  .details__line { font-size: 13.5px; line-height: 18px; }
  .details__key { color: var(--green); font-weight: 700; }
  .details__web { color: var(--green); }
  .accent {
    position: absolute;
    width: 34px;
    height: 50px;
    background: var(--green);
    border-right: 4px solid var(--teal);
  }
  .accent--left { left: 0; top: 150px; }
  .accent--right { right: 0; top: 40px; border-right: none; border-left: 4px solid var(--teal); }
  .brand {
    position: absolute;
    inset: 0;
    display: flex;
    align-items: center;
    justify-content: center;
    gap: 12px;
  }
  .brand__mark {
    width: 22px; height: 22px;
    background: var(--green);
  }
  .brand__name {
    font-weight: 700;
    font-size: 34px;
    letter-spacing: 6px;
    color: var(--white);
  }
</style>
</head>
<body>
  <section class="card card--back">
    <div class="band band--top"></div>
    <div class="details">
      <div class="details__name">MARLON TEAGUE</div>
      <div class="details__role">Managing Director</div>
      <div class="details__rule"></div>
      <div class="details__line"><span class="details__key">P:</span> 044-987 654 321</div>
      <div class="details__line"><span class="details__key">M:</span> 044-987 654 321</div>
      <div class="details__line"><span class="details__key">E:</span> info@bravelmail.com</div>
      <div class="details__line details__web">www.bravelacres.com</div>
      <div class="details__rule"></div>
      <div class="details__line">2817 W 68th N St</div>
      <div class="details__line">Tulsa, OK 74592</div>
    </div>
    <div class="band band--bottom"></div>
  </section>

  <section class="card card--front">
    <div class="accent accent--left"></div>
    <div class="accent accent--right"></div>
    <div class="brand">
      <span class="brand__mark"></span>
      <span class="brand__name">BRAVEL ACRES</span>
    </div>
  </section>
</body>
</html>
```